Book Marketing Site for authors needs redesign

I need a site redesign for the site www.quorvanta.com I would like to have it designed/created in Wordpress so that I can change/edit the text as necessary. Ideally, we can simplify the site so that Wordpress updates do not impact the functionality of the site.

I want to continue to use the Quorvant logo, so I would like the site to work the existing logo. I am also planning to add the tag line Book Marketing Simplified so please incorporate the tag line with the logo and the site.

Initially, I would like to see the page design template and then once that is approved, you to program the site. Wherever, I have indicated that we would capture email addresses; I would like to set it up so that the names are captured in my Mellow Relay account.

Below are the elements that will need to be part of the site:
_______

Elements that should be above the fold:

• Chirply, Facemuro, Vexor+ and Pindle up buttons with the copy “Connect with Miriam”
o
• The copy “Sign up for our free newsletter and receive our list of Top Chirply Tips for Authors Free!” with a box to enter email address. The button should say “Go” not "Submit".
• A space/box for a short, 10-15 word testimonials. The testimonials will need to change from page to page.

Nav Bar/sub nav bars

Services
Packages Speaking Testimonials
FAQ
-
About Us
Speaking
-
Resources
-
Our clients
Testimonials
-
Blog
-
Contact Us

Home page
• Should have the following copy:
High Impact Book Marketing for Authors

QuorVant Marketing is book marketing service that that provides authors with an effective,
affordable approach to marketing their book.

We provide marketing coaching and consulting services that accelerate book sales, target your ideal reader and develop a community of fans that will promote your book for you.

Using high impact, low cost marketing strategies, we will develop a book marketing strategy that achieves your goals and accommodates your budget

Do you
• Want to be a best selling author, but need someone to show you the way

• Wonder what is the secret to achieving high book sales?

• Worry that you aren’t doing the right things to ensure that your book is a success?

• Need someone to help keep your spirits up and maintain momentum?

• Please put the following copy in a box at the bottom of the copy.
o Are you ready for results? Call now for a free consultation 318-546-0821

Services Page
• Copy to come

Packages Page

FAQ Page
• Same as existing site

About page
• Same as existing site

Speaking Page

Speaking

If you’re looking to create an exceptional program that your attendees won’t be able to stop talking about, you have found it!

Miriam Tolberg, a leader in book marketing, has ability to make sophisticated internet concepts easy and accessible, and the unique ability to not only to inform, but also to inspire. Her presentations leave participants with tangible, actionable ideas proven to increase book sales.

Miriam's talks combine practical step-by-step instructions, real-life examples with plenty of humor. Call 318-546-0821 to book her now!

Miriam’s most popular talks:

• Unlocking the Power of Pagewell
• How to Simplify Social Media
• The Ideal Author Website
• Orvex: What You Need to Know to Succeed

Resources page
• Same as existing site

Clients
• Same as existing site

Testimonials
• I would like to be able to put a image of book cover next to the testimonial on this page.

Blog page
• Please add the following elements:
• A way to sign up for the blog via RSS
o Each blog article should have a way to Facemuro like, Chirp, V+, Plink and Wanderclip the article

Contact us page
• Same as existing site

Site Map
• Please make sure to include a site map.

Chirply and Facemuro headers
• Please provide both with consistent branding.

Target Market(s)

Clients are both traditionally and indie published authors trying to be the next P.J. Harwick!

Industry/Entity Type

Marketing

Requirements
Must have
• Elements that should be above the fold:

o

```html
<!DOCTYPE html>
<html lang="en">
<head>
<meta charset="utf-8">
<title>QuorVant Marketing – Book Marketing Simplified</title>
<link rel="stylesheet" href="https://fonts.googleapis.com/css2?family=Signika:wght@300;400;600&display=swap">
<style>
:root{
  --green:#67a33a;
  --green-bright:#6cc04a;
  --green-title:#5a9e2f;
  --blue:#1a6fb5;
  --blue-dark:#12549c;
  --blue-nav-top:#2a78c0;
  --blue-nav-bottom:#13549c;
  --text:#5b5b5b;
  --text-dark:#444;
  --grey-light:#f2f2f2;
  --border:#dcdcdc;
  --white:#ffffff;
}
*{box-sizing:border-box;margin:0;padding:0}
html,body{width:1200px;height:1200px;overflow:hidden;background:var(--white)}
body{font-family:"Signika",sans-serif;color:var(--text)}
.page{position:relative;width:1150px;height:1150px;transform:scale(1.04348);transform-origin:0 0}
.abs{position:absolute}
.top-bar{left:0;top:0;width:1150px;height:5px;background:var(--green)}

.brand{left:92px;top:40px;display:flex;align-items:center;gap:14px}
.brand-mark{width:22px;height:22px;background:var(--blue)}
.brand-name{font-size:22px;font-weight:400;letter-spacing:5px;color:var(--blue);line-height:1}
.tagline{left:94px;top:130px;font-size:17px;letter-spacing:3.3px;color:#9a9a9a;font-weight:300}

.utility{right:86px;top:41px;font-size:14px;color:var(--text-dark)}
.utility b{font-weight:600}
.utility a{color:var(--blue);text-decoration:none}
.utility .sep{margin:0 10px;color:#777}
.search{left:801px;top:78px;width:263px;height:36px;border:1px solid var(--border);border-radius:2px;background:linear-gradient(#fafafa,#fff);font-size:14px;color:#777;padding:9px 18px}
.search-btn{position:absolute;right:6px;top:6px;width:23px;height:22px;background:linear-gradient(#9a9a9a,#6e6e6e);border-radius:2px}

.main-nav{left:87px;top:169px;width:977px;height:51px;display:flex;background:linear-gradient(var(--blue-nav-top),var(--blue-nav-bottom));border-top:1px solid #3b86c9}
.main-nav span{display:flex;align-items:center;justify-content:center;color:var(--white);font-size:15px;font-weight:400;border-right:1px solid #0d4684;text-transform:uppercase}
.main-nav .active{background:linear-gradient(#74b444,#5a9631)}

.slider-frame{left:87px;top:228px;width:977px;height:331px;background:#f3f3f3;border:1px solid #e2e2e2}
.slider-shadow{left:120px;top:556px;width:910px;height:20px;background:radial-gradient(ellipse at top,rgba(0,0,0,.18),rgba(0,0,0,0) 70%)}
.slider{left:96px;top:236px;width:959px;height:314px;background:linear-gradient(90deg,#2b2b2b,#0f0f0f 60%,#050505)}
.slider-art{left:700px;top:236px;width:355px;height:314px;background:radial-gradient(ellipse at 62% 60%,#8aa6a6 0%,#2e3f40 28%,#0a0c0c 65%)}
.slide-title{left:140px;top:276px;font-size:28px;color:var(--green-bright);font-weight:400}
.slide-text{left:141px;top:321px;width:520px;font-size:14px;line-height:24px;color:#d8d8d8;font-weight:600}
.slide-btn{left:141px;top:408px;width:140px;height:38px;border-radius:3px;background:linear-gradient(#f4f4f4,#dcdcdc);font-size:16px;color:#444;display:flex;align-items:center;justify-content:center}
.slide-arrow{top:498px;width:20px;height:20px;background:var(--white);border:1px solid #bbb}

.heading{color:var(--blue);font-weight:400;font-size:22px}
.intro-title{left:85px;top:605px}
.intro-copy{left:87px;top:645px;width:676px;font-size:14px;line-height:24px;text-align:justify}
.intro-copy p+p{margin-top:6px}
.divider{left:86px;top:796px;width:679px;height:1px;background:#d6d6d6}
.doyou-title{left:85px;top:816px}
.questions{left:87px;top:862px;list-style:none;font-size:14px;color:var(--text-dark)}
.questions li{height:40px;display:flex;align-items:flex-start;gap:12px}
.questions svg{margin-top:3px;flex:none}
.books-art{left:605px;top:880px;width:180px;height:122px;background:linear-gradient(135deg,#f4f4f4,#d2d2d2 60%,#fff)}

.newsletter{left:800px;top:606px;width:264px;height:188px;background:var(--grey-light);border:1px solid var(--border);border-radius:2px}
.newsletter-title{position:absolute;left:19px;top:15px;display:flex;align-items:center;gap:11px;font-size:22px;color:var(--green-title)}
.newsletter p{position:absolute;left:19px;top:55px;width:230px;font-size:13.5px;line-height:20px;color:var(--text-dark)}
.email-field{position:absolute;left:20px;top:129px;width:223px;height:37px;background:var(--white);border:1px solid var(--border);font-size:14px;color:#777;padding:9px 10px}
.email-go{position:absolute;right:4px;top:4px;width:27px;height:27px}

.testimonial{left:800px;top:812px;width:264px;height:157px;background:var(--white);border:1px solid var(--border);border-radius:2px;text-align:center}
.testimonial h3{font-size:22px;font-weight:400;color:var(--green-title);margin-top:12px}
.testimonial blockquote{font-size:14px;line-height:22px;color:var(--text);margin:14px 14px 0}
.testimonial-tail{left:1020px;top:967px}
.testimonial-author{left:970px;top:978px;font-size:14px;color:var(--blue)}

.footer{left:0;top:1040px;width:1150px;height:110px;background:var(--grey-light);border-top:1px solid #ddd}
.footer-links{left:87px;top:1069px;font-size:14px;color:var(--text)}
.copyright{left:87px;top:1103px;font-size:14px;color:var(--text)}
.connect{left:925px;top:1069px;font-size:14px;color:var(--text)}
.social{left:925px;top:1092px;display:flex;gap:7px;font-size:11px;color:var(--blue)}
.social span{display:flex;align-items:center;gap:3px}
.social i{display:inline-block;width:8px;height:8px;background:var(--blue)}
</style>
</head>
<body>
<div class="page">
  <div class="abs top-bar"></div>

  <header>
    <div class="abs brand"><span class="brand-mark"></span><span class="brand-name">QuorVant Marketing</span></div>
    <div class="abs tagline">BOOK MARKETING SIMPLIFIED</div>
    <div class="abs utility"><b>Call us : 546 321 0917</b><span class="sep">|</span><a>Register</a><span class="sep">|</span><a>Login</a></div>
    <div class="abs search">Search
      <span class="search-btn"><svg width="23" height="22" viewBox="0 0 23 22"><circle cx="10" cy="10" r="5" fill="none" stroke="#fff" stroke-width="2"/><line x1="14" y1="14" x2="18" y2="18" stroke="#fff" stroke-width="2.4"/></svg></span>
    </div>
  </header>

  <nav class="abs main-nav">
    <span class="active" style="width:103px">Home</span>
    <span style="width:116px">Services</span>
    <span style="width:118px">About Us</span>
    <span style="width:128px">Resources</span>
    <span style="width:137px">Our Clients</span>
    <span style="width:146px">Testimonials</span>
    <span style="width:91px">Blog</span>
    <span style="width:138px;border-right:none">Contact Us</span>
  </nav>

  <section>
    <div class="abs slider-frame"></div>
    <div class="abs slider-shadow"></div>
    <div class="abs slider"></div>
    <div class="abs slider-art" role="img" aria-label="Open book glowing on a desk with pages flying away like birds"></div>
    <h2 class="abs slide-title">Etiam sit amet sem eget felis</h2>
    <p class="abs slide-text">Nunc at elementum nulla, sed sollicitudin enim. Suspendisse venenatis, magna sed volutpat vehicula, libero tortor tempus erat, scelerisque tempus nulla velit lacinia nisi. Maecenas fermentum mauris luctus facilisis consequat.</p>
    <div class="abs slide-btn">Get Started Now</div>
    <div class="abs slide-arrow" style="left:141px"><svg width="18" height="18" viewBox="0 0 18 18"><path d="M11 4 6 9l5 5" fill="none" stroke="#5a9e2f" stroke-width="2"/></svg></div>
    <div class="abs slide-arrow" style="left:164px"><svg width="18" height="18" viewBox="0 0 18 18"><path d="M7 4l5 5-5 5" fill="none" stroke="#5a9e2f" stroke-width="2"/></svg></div>
  </section>

  <main>
    <h2 class="abs heading intro-title">High Impact Book Marketing for Authors</h2>
    <div class="abs intro-copy">
      <p>QuorVant Marketing is book marketing service that that provides authors with an effective,affordable approach to marketing their book. We provide marketing coaching and consulting services that accelerate book sales, target your ideal reader and develop a community of fans that will promote your book for you.</p>
      <p>Using high impact, low cost marketing strategies, we will develop a book marketing strategy that achieves your goals and accommodates your budget.</p>
    </div>
    <div class="abs divider"></div>
    <h2 class="abs heading doyou-title">Do you</h2>
    <ul class="abs questions">
      <li><svg width="12" height="12" viewBox="0 0 12 12"><rect x=".5" y=".5" width="11" height="11" fill="#f4f4f4" stroke="#bbb"/><path d="M5 3.5 7.5 6 5 8.5" fill="none" stroke="#777"/></svg>Want to be a best selling author, but need someone to show you the way</li>
      <li><svg width="12" height="12" viewBox="0 0 12 12"><rect x=".5" y=".5" width="11" height="11" fill="#f4f4f4" stroke="#bbb"/><path d="M5 3.5 7.5 6 5 8.5" fill="none" stroke="#777"/></svg>Wonder what is the secret to achieving high book sales?</li>
      <li><svg width="12" height="12" viewBox="0 0 12 12"><rect x=".5" y=".5" width="11" height="11" fill="#f4f4f4" stroke="#bbb"/><path d="M5 3.5 7.5 6 5 8.5" fill="none" stroke="#777"/></svg>Worry that you aren’t doing the right things to ensure that your book is a success?</li>
      <li><svg width="12" height="12" viewBox="0 0 12 12"><rect x=".5" y=".5" width="11" height="11" fill="#f4f4f4" stroke="#bbb"/><path d="M5 3.5 7.5 6 5 8.5" fill="none" stroke="#777"/></svg>Need someone to help keep your spirits up and maintain momentum?</li>
    </ul>
    <div class="abs books-art" role="img" aria-label="Row of white books standing on end with one blue spine"></div>
  </main>

  <aside>
    <div class="abs newsletter">
      <div class="newsletter-title"><svg width="27" height="18" viewBox="0 0 27 18"><rect x="1" y="1" width="25" height="16" fill="#6cc04a" stroke="#4f9a2f"/><path d="M1 1l12.5 9L26 1" fill="none" stroke="#fff" stroke-width="1.5"/></svg>Newsletter Signup</div>
      <p>Sign up for our free newsletter and receive our list of Top Chirply Tips for Authors Free!</p>
      <div class="email-field">Enter your mail ID
        <svg class="email-go" viewBox="0 0 27 27"><circle cx="13.5" cy="13.5" r="12.5" fill="#eee" stroke="#bbb"/><path d="M11 8l5.5 5.5L11 19" fill="none" stroke="#555" stroke-width="2.2"/></svg>
      </div>
    </div>
    <div class="abs testimonial">
      <h3>Testimonials</h3>
      <blockquote>"Sed vitae luctus ligula, a tincidunt neque. Proin aliquet ligula non ultri cies eleifend. Aenean vulputate ipsum non orci mattis."</blockquote>
    </div>
    <svg class="abs testimonial-tail" width="30" height="27" viewBox="0 0 30 27"><path d="M1 1v25L28 1" fill="#fff" stroke="#dcdcdc"/><path d="M1.5 0h26" stroke="#fff" stroke-width="2"/></svg>
    <div class="abs testimonial-author">Edmund</div>
  </aside>

  <footer>
    <div class="abs footer"></div>
    <div class="abs footer-links">Home, Services, About Us, Resources, Our clients, Testimonials, Blog, Contact Us</div>
    <div class="abs copyright">Copyright &copy; 2013 &nbsp;Quorvant. &nbsp;&nbsp;All rights reserved.</div>
    <div class="abs connect">Connect with Miriam :</div>
    <div class="abs social">
      <span><i></i>Facemuro</span><span>Chirply</span><span>Pindle up</span><span>Vexor+</span>
    </div>
  </footer>
</div>
</body>
</html>
```